We are a doctors medical practice
I need the business card to be eye catching and memorable,
to reflect professionalism, yet also warmth and care

the numbers need to be easy to see, for the elderly

and the logo also in a location that is large enough to see and be eye catching

Back of card:
opening hours:
Mon- Fri 8.30am to 6pm
Sat 9am to 4pm

rows for appontments, date and time
Updates

HiĀ 

Modification to company name

BROOKVALE KINDRED HEALTH MEDICAL PRACTICE

Thanks
Marla

Reason: I am look for a unique design that also fulfils the design brief

I have attempted to post a .eps and .ai file of the logo

Target Market(s)

needs to appeal to the majority, mainly adults

Industry/Entity Type

Medical

Contact Information for Business Card

company name: Brookvale Kindred Health Medical Practice
Name: Dr Marla Vossberg-Tait
Qualifications: MBBS, Bsci(med), FRACGP, DCH, SH&FPA, Dip Derm
Address: Shop 3/41-43 Quorrow St, Brookvale 2940
Ph: 02 9418 3052
Fax: 02 9461 8824

Requirements
Nice to have
• I like balance
gold/ silver incorporated, as well as the other colours in the logo- but not limited to these colours
a "medical" feel
Should not have
• dark or strong colours

```html
<!DOCTYPE html>
<html lang="en">
<head>
<meta charset="utf-8">
<title>Brookvale Kindred Health Medical Practice – Business Card</title>
<link rel="stylesheet" href="https://fonts.googleapis.com/css2?family=Open+Sans:wght@400;700&family=Roboto+Condensed:wght@700&family=Tinos&display=swap">
<style>
  :root{
    --stage:#3a3c3e;
    --card:#ffffff;
    --blue:#0a84f0;
    --navy:#1b3fd6;
    --pink:#f04fd8;
    --green:#7ad323;
    --phone-green:#5cc41e;
    --grey:#8a8a8a;
    --ink:#111111;
    --shadow:rgba(0,0,0,.45);
  }
  *{box-sizing:border-box;margin:0;padding:0}
  html,body{width:1200px;height:892px;overflow:hidden}
  body{background:var(--stage);position:relative;font-family:"Open Sans",Arial,sans-serif}

  .card{position:absolute;background:var(--card);box-shadow:0 6px 18px var(--shadow);overflow:hidden}

  /* ---------- Back: appointment card ---------- */
  .card--back{left:480px;top:115px;width:460px;height:285px;padding:16px 22px 0 22px}
  .hours{display:flex;align-items:center;gap:10px;color:var(--blue);font-size:16px;height:32px}
  .hours__clock{width:30px;height:30px;flex:none}
  .hours__divider{width:3px;height:26px;background:var(--green);margin:0 4px}
  .slot{position:relative;height:58px;border-bottom:2px solid var(--blue);margin-top:8px}
  .slot__days{position:absolute;left:24px;right:0;top:8px;display:flex;justify-content:space-between;color:var(--grey);font-size:14px}
  .slot__date,.slot__at,.slot__ampm{position:absolute;bottom:3px;color:var(--ink);font-size:14px;font-weight:700}
  .slot__date{left:0}
  .slot__at{left:176px}
  .slot__ampm{right:4px}
  .notice{margin-top:10px;text-align:center;font-family:"Tinos","Times New Roman",serif;font-size:15px;line-height:20px;color:var(--ink)}

  /* ---------- Front: business card ---------- */
  .card--front{left:250px;top:420px;width:500px;height:300px}
  .front__bg{position:absolute;inset:0;width:100%;height:100%}
  .brand{position:absolute;left:14px;top:20px;width:210px;text-align:center}
  .brand__disc{width:120px;height:120px;border-radius:50%;margin:0 auto 16px;background:var(--blue)}
  .brand__name{font-family:"Roboto Condensed","Arial Narrow",sans-serif;font-weight:700;color:var(--navy);font-size:16px;line-height:1.1;letter-spacing:.3px}
  .doctor{position:absolute;right:16px;top:20px;text-align:right;color:#fff}
  .doctor__name{font-weight:700;font-size:17px}
  .doctor__quals{font-size:10px;line-height:1.35;margin-top:6px}
  .contacts{position:absolute;right:16px;top:180px;color:#fff;text-align:right}
  .contact{display:flex;align-items:center;justify-content:flex-end;gap:6px;font-weight:700;font-size:22px;line-height:1.3}
  .contact__icon{width:22px;height:22px;flex:none}
  .contacts__rule{height:2px;background:var(--pink);margin:4px 0 0 -10px}
  .address{position:absolute;right:16px;top:242px;color:#fff;text-align:right;font-family:"Roboto Condensed","Arial Narrow",sans-serif;font-weight:700;font-size:19px;line-height:1.25}
</style>
</head>
<body>

<section class="card card--back" aria-label="Appointment card">
  <div class="hours">
    <svg class="hours__clock" viewBox="0 0 30 30" aria-hidden="true">
      <circle cx="15" cy="15" r="14" fill="var(--blue)"/>
      <circle cx="15" cy="15" r="10" fill="#fff"/>
      <path d="M15 8v7l-4 4" stroke="var(--blue)" stroke-width="2" fill="none" stroke-linecap="round"/>
    </svg>
    <span>Mon- Fri 8:30am to 6pm</span>
    <span class="hours__divider"></span>
    <span>Sat 9am to 4pm</span>
  </div>

  <div class="slot">
    <div class="slot__days"><span>Mon.</span><span>Tues.</span><span>Wed.</span><span>Thurs.</span><span>Fri.</span><span>Sat.</span></div>
    <span class="slot__date">Date:</span><span class="slot__at">AT</span><span class="slot__ampm">A.M./P.M.</span>
  </div>
  <div class="slot">
    <div class="slot__days"><span>Mon.</span><span>Tues.</span><span>Wed.</span><span>Thurs.</span><span>Fri.</span><span>Sat.</span></div>
    <span class="slot__date">Date:</span><span class="slot__at">AT</span><span class="slot__ampm">A.M./P.M.</span>
  </div>
  <div class="slot">
    <div class="slot__days"><span>Mon.</span><span>Tues.</span><span>Wed.</span><span>Thurs.</span><span>Fri.</span><span>Sat.</span></div>
    <span class="slot__date">Date:</span><span class="slot__at">AT</span><span class="slot__ampm">A.M./P.M.</span>
  </div>

  <p class="notice">Please call if you are unable to make your appointment</p>
</section>

<section class="card card--front" aria-label="Business card">
  <svg class="front__bg" viewBox="0 0 500 300" preserveAspectRatio="none" aria-hidden="true">
    <path d="M222 0 C272 100 248 230 80 300 L150 300 C258 230 280 100 232 0Z" fill="var(--pink)"/>
    <path d="M234 0 C288 100 268 230 155 300 L172 300 C282 230 302 100 246 0Z" fill="var(--green)"/>
    <path d="M246 0 C302 100 282 230 172 300 L500 300 L500 0Z" fill="var(--blue)"/>
  </svg>

  <div class="brand">
    <div class="brand__disc"></div>
    <p class="brand__name">BROOKVALE KINDRED HEALTH<br>MEDICAL PRACTICE</p>
  </div>

  <div class="doctor">
    <p class="doctor__name">Dr Marla Vossberg-Tait</p>
    <p class="doctor__quals">MBBS, Bsci(med), FRACGP, DCH,<br>SH&amp;FPA, Dip Derm</p>
  </div>

  <div class="contacts">
    <p class="contact">
      <svg class="contact__icon" viewBox="0 0 22 22" aria-label="Phone">
        <circle cx="11" cy="11" r="11" fill="var(--phone-green)"/>
        <path d="M7.5 5.5l2 2.5-1.2 1.5c.8 1.8 2.2 3.2 4 4l1.5-1.2 2.5 2-1.3 2c-4.5-.3-8.7-4.5-9-9z" fill="#fff"/>
      </svg>
      02 9418 3052
    </p>
    <p class="contact">
      <svg class="contact__icon" viewBox="0 0 22 22" aria-label="Fax">
        <circle cx="11" cy="11" r="11" fill="var(--phone-green)"/>
        <rect x="7" y="5" width="8" height="5" fill="#fff"/>
        <rect x="5" y="10" width="12" height="7" rx="1" fill="#fff"/>
        <rect x="8" y="12" width="6" height="1.5" fill="var(--phone-green)"/>
      </svg>
      02 9461 8824
    </p>
    <div class="contacts__rule"></div>
  </div>

  <p class="address">Shop 3/41-43 Quorrow St,<br>Brookvale 2940</p>
</section>

</body>
</html>
```